Business Card Design for Portrait photography professional

We are a small company specializing in portrait photography (weddings, family, couples, children, newborn, pregnant, etc.) Occasionally we do business portraits too and do some other type of photography. We need a business card which would fit into the same look and feel as our website theme (lumvika.com - under construction currently).
Our target customer base lies within mid- to upmarket. We want our business cards to convey a feeling of quality, solidness and a bit luxury.
Design should be universal and usable on 85mmx55mm, 90mmx50mm and 90mmx55mm
one extra file (PSD of a website didn't fit into the allowed updoad, therefore has put it into my filecrate: https://www.filecrate-example.net/s/qt7wk2rbvx9dmhe/website%20theme%20PSD.psd)

Target Market(s)

mostly private people, 25-60 years old, mostly well established.

Industry/Entity Type

Portrait Photography

Requirements
Must have
• 2 sided design (print on both sides of the business card).
Must include:
business name, logo, URL (lumvika.no) , employee name, email address, and phone number.
Colorscheme of the website lumvika.no / lumvika.com

```html
<!DOCTYPE html>
<html lang="en">
<head>
<meta charset="utf-8">
<title>Lumvika Portraits — Business Card</title>
<link rel="stylesheet" href="https://fonts.googleapis.com/css2?family=Questrial&family=Baumans&display=swap">
<style>
  :root {
    --backdrop: #2b2a2a;
    --card-red: #ec1f27;
    --card-red-glow: #f36a3c;
    --card-dark: #242020;
    --card-dark-glow: #4a4644;
    --ink-light: #f4f1ec;
    --accent-red: #d8282e;
    --rule-red: #a8262a;
  }
  * { margin: 0; padding: 0; box-sizing: border-box; }
  html, body {
    width: 1200px; height: 900px; overflow: hidden;
    background: var(--backdrop);
  }
  .canvas {
    position: relative; width: 1200px; height: 900px;
    font-family: "Questrial", sans-serif;
  }
  .card {
    position: absolute; top: 298px;
    width: 500px; height: 304px;
    border: 1px solid rgba(255,255,255,0.55);
    overflow: hidden;
  }
  /* Front: red side */
  .card--front {
    left: 70px;
    background: radial-gradient(circle at 50% 48%, var(--card-red-glow) 0%, var(--card-red) 42%, var(--card-red) 100%);
  }
  .front-mark {
    position: absolute; inset: 0;
    display: flex; flex-direction: column; align-items: center; justify-content: center;
    gap: 14px;
  }
  .front-mark__circle {
    width: 112px; height: 112px; border-radius: 50%;
    border: 4px solid var(--ink-light);
  }
  .front-mark__name {
    color: var(--ink-light); font-size: 22px; letter-spacing: 0.5px;
  }
  /* Back: dark side */
  .card--back {
    left: 630px;
    background: radial-gradient(circle at 48% 50%, var(--card-dark-glow) 0%, var(--card-dark) 60%, #1e1b1a 100%);
  }
  .brand {
    position: absolute; left: 43px; top: 56px;
    display: flex; align-items: center; gap: 16px;
  }
  .brand__circle {
    width: 50px; height: 50px; border-radius: 50%;
    border: 2px solid var(--ink-light);
  }
  .brand__name {
    color: var(--ink-light); font-size: 27px; letter-spacing: 0.2px;
  }
  .contact {
    position: absolute; left: 330px; top: 190px;
    color: var(--ink-light); font-size: 13px;
  }
  .contact__person {
    font-family: "Baumans", sans-serif; color: var(--accent-red);
    font-size: 17px; margin-bottom: 12px; letter-spacing: 0.4px;
  }
  .contact__row { display: flex; align-items: center; gap: 6px; margin-bottom: 7px; }
  .contact__icon { width: 11px; height: 13px; flex: none; }
  .footer {
    position: absolute; left: 9px; right: 9px; top: 272px;
    display: flex; align-items: center; gap: 24px;
  }
  .footer__rule { flex: 1; height: 1px; background: var(--rule-red); }
  .footer__url { color: var(--accent-red); font-size: 14px; letter-spacing: 0.4px; }
</style>
</head>
<body>
<main class="canvas">
  <section class="card card--front" aria-label="Business card front">
    <div class="front-mark">
      <div class="front-mark__circle"></div>
      <div class="front-mark__name">Lumvika Portraits</div>
    </div>
  </section>

  <section class="card card--back" aria-label="Business card back">
    <div class="brand">
      <div class="brand__circle"></div>
      <div class="brand__name">Lumvika Portraits</div>
    </div>

    <div class="contact">
      <div class="contact__person">K.M. Halvorsen</div>
      <div class="contact__row">
        <svg class="contact__icon" viewBox="0 0 11 13" aria-hidden="true">
          <rect x="0.5" y="1.5" width="10" height="10" fill="#bdb8b4"/>
          <text x="5.5" y="9.5" font-size="8" text-anchor="middle" fill="#242020" font-family="sans-serif">e</text>
        </svg>
        <span>: info@lumvika.no</span>
      </div>
      <div class="contact__row">
        <svg class="contact__icon" viewBox="0 0 11 13" aria-hidden="true">
          <rect x="2.5" y="0.5" width="6" height="12" rx="1" fill="#bdb8b4"/>
          <rect x="3.5" y="2" width="4" height="4" fill="#242020"/>
        </svg>
        <span>: (+47) 412-30-586</span>
      </div>
    </div>

    <div class="footer">
      <div class="footer__rule"></div>
      <div class="footer__url">www.lumvika.no</div>
      <div class="footer__rule"></div>
    </div>
  </section>
</main>
</body>
</html>
```